Design Business Card with our Logo

We have changed our firm name from Halbrook, Penney & Ostrand, PLLC to Halbrook, Penney & Vantrell, LLP and now need to re-design our business cards. I have attached an image of our old card so that you can see the style that we like -- clean, modern, colorful and professional. We were not thrilled with the fonts that we used on the old card, so feel free to use more modern fonts. I also attached a copy of the new logo shape, which is similar to the old one; and some other card ideas that we found in the gigcrafter.com showcase that looked nice to us. Please feel free to try different colors as we are not tied down to orange or blue. Looking for fresh new ideas.

```html
<!DOCTYPE html>
<html lang="en">
<head>
<meta charset="utf-8">
<title>Halbrook, Penney & Vantrell, LLP — Business Card</title>
<link href="https://fonts.googleapis.com/css2?family=Montserrat:wght@400;500;600;700&display=swap" rel="stylesheet">
<style>
  :root {
    --orange: #f26a1b;
    --ink: #1d1d1f;
    --card-white: #f7f7f5;
    --card-black: #1e1c1b;
    --muted: #4a4a4a;
    --back-text: #d8d8d8;
    --stage: #e4e6ea;
  }
  * { margin: 0; padding: 0; box-sizing: border-box; }
  html, body { width: 1200px; height: 900px; overflow: hidden; }
  body {
    background: var(--stage);
    font-family: "Montserrat", sans-serif;
    display: flex;
    align-items: center;
    justify-content: center;
    gap: 40px;
  }
  .card {
    position: relative;
    width: 540px;
    height: 309px;
    overflow: hidden;
    border-bottom: 6px solid var(--orange);
  }

  /* Front */
  .card-front { background: var(--card-white); color: var(--ink); }
  .front-band-top {
    position: absolute; left: 0; top: 0;
    width: 18px; height: 150px; background: var(--orange);
  }
  .front-band-top::after {
    content: ""; position: absolute; left: 18px; top: 0;
    width: 12px; height: 150px;
    background: linear-gradient(to bottom, var(--orange) 0 90%, transparent 90%);
    clip-path: polygon(0 0, 100% 0, 100% 88%, 0 100%);
  }
  .front-band-bottom {
    position: absolute; left: 0; top: 160px; bottom: 0;
    width: 8px; background: var(--orange);
  }
  .firm {
    position: absolute; left: 56px; top: 32px;
    display: flex; align-items: flex-start; gap: 12px;
  }
  .firm-mark { width: 46px; height: 46px; background: var(--orange); flex: none; }
  .firm-name {
    font-weight: 700; font-size: 15px; line-height: 1.05;
    letter-spacing: 0.5px; text-transform: uppercase; color: var(--ink);
  }
  .firm-tag {
    margin-top: 4px; font-size: 8.5px; font-weight: 500;
    letter-spacing: 2.4px; text-transform: uppercase; color: var(--orange);
  }
  .person { position: absolute; left: 40px; top: 150px; }
  .person-name {
    font-weight: 600; font-size: 14px; letter-spacing: 0.6px;
    text-transform: uppercase; color: var(--orange);
  }
  .person-role { font-size: 10.5px; color: var(--muted); margin-top: 2px; }
  .contact {
    position: absolute; right: 70px; top: 150px;
    list-style: none; font-size: 11px; color: var(--ink);
  }
  .contact li { display: flex; align-items: flex-start; gap: 9px; margin-bottom: 6px; line-height: 1.3; }
  .contact .icon {
    width: 17px; height: 17px; background: var(--orange); flex: none;
    display: flex; align-items: center; justify-content: center;
  }
  .contact svg { width: 11px; height: 11px; }

  /* Back */
  .card-back { background: var(--card-black); color: var(--back-text); }
  .services {
    position: absolute; left: 26px; top: 30px;
    border-left: 2px solid var(--orange); padding-left: 10px;
    list-style: none; font-size: 10px; line-height: 1.55;
  }
  .services li:first-child { text-transform: uppercase; letter-spacing: 1px; }
  .back-brand {
    position: absolute; left: 50%; top: 50%; transform: translate(-50%, -50%);
    display: flex; align-items: center; gap: 10px;
  }
  .back-mark { width: 30px; height: 30px; background: var(--orange); }
  .back-name {
    font-weight: 700; font-size: 13px; letter-spacing: 0.8px;
    text-transform: uppercase; color: var(--orange);
  }
  .website {
    position: absolute; left: 26px; bottom: 20px;
    display: flex; align-items: center; gap: 7px; font-size: 10.5px;
  }
  .website-dot { width: 9px; height: 9px; background: var(--orange); }
</style>
</head>
<body>
  <section class="card card-front">
    <div class="front-band-top"></div>
    <div class="front-band-bottom"></div>

    <div class="firm">
      <div class="firm-mark"></div>
      <div>
        <div class="firm-name">Halbrook<br>Penney<br>Vantrell</div>
        <div class="firm-tag">Attorneys at Law</div>
      </div>
    </div>

    <div class="person">
      <div class="person-name">Grant L. Penney</div>
      <div class="person-role">Partner</div>
    </div>

    <ul class="contact">
      <li>
        <span class="icon"><svg viewBox="0 0 12 12"><path d="M2.5 1h2l1 2.6-1.3.9a6 6 0 0 0 3.3 3.3l.9-1.3 2.6 1v2A1.4 1.4 0 0 1 9.6 11 8.6 8.6 0 0 1 1 2.4 1.4 1.4 0 0 1 2.5 1z" fill="#fff"/></svg></span>
        555.210.4460
      </li>
      <li>
        <span class="icon"><svg viewBox="0 0 12 12"><rect x="1" y="2.5" width="10" height="7" fill="none" stroke="#fff" stroke-width="1.2"/><path d="M1 2.8 6 6.6l5-3.8" fill="none" stroke="#fff" stroke-width="1.2"/></svg></span>
        gpenney@hpvlegal.com
      </li>
      <li>
        <span class="icon"><svg viewBox="0 0 12 12"><path d="M6 11S2 6.8 2 4.4a4 4 0 0 1 8 0C10 6.8 6 11 6 11z" fill="#fff"/><circle cx="6" cy="4.4" r="1.4" fill="#f26a1b"/></svg></span>
        27 Harbor Line Avenue<br>Port Merrow Florida 30918
      </li>
    </ul>
  </section>

  <section class="card card-back">
    <ul class="services">
      <li>Business</li>
      <li>Real Estate and Construction</li>
      <li>Injury and Insurance Claims</li>
    </ul>

    <div class="back-brand">
      <div class="back-mark"></div>
      <div class="back-name">Halbrook Penney Vantrell</div>
    </div>

    <div class="website">
      <span class="website-dot"></span>
      www.hpvlegal.com
    </div>
  </section>
</body>
</html>
```